DUVNA Powerpoint Template

A powerpoint template for our new brand of private label components which are built for us in Asia. We are looking for a fresh design for our powerpoint template. Note the subtle overlay of the fox in our theme. We like this as it implies quickness. Do not overuse the fox theme. It needs to be very subtle if used.

Our products include High performance passive RF and Fiber components and cable solutions for the wireless industry. Our comprehensive product portfolios include both general and low PIM grades and are widely used for cellular towers and in-building DAS systems as well as in the wireless research and development labs.

Common models include:
Filters
Diplexers, triplexers and 5plexers
Splitters and combiners
Signal tappers
Couplers
Terminations load and attenuators
Jumper cables and testing cables assemblies
Fiber Splice Trays
Patch Panels
Fiber Jumpers & Adapters

```html
<!DOCTYPE html>
<html lang="en">
<head>
<meta charset="utf-8">
<title>DUVNA Presentation Slide</title>
<link href="https://fonts.googleapis.com/css2?family=Roboto+Condensed:wght@400;700&family=Carlito:wght@400;700&display=swap" rel="stylesheet">
<style>
  :root {
    --brand-red: #dc0009;
    --ink: #111111;
    --body-text: #3a3a3a;
    --tint: #fdf0f1;
    --rule: #f3c9cc;
    --white: #ffffff;
  }
  * { margin: 0; padding: 0; box-sizing: border-box; }
  html, body { width: 1200px; height: 900px; overflow: hidden; background: var(--white); }
  .slide {
    position: relative;
    width: 1200px;
    height: 900px;
    overflow: hidden;
    font-family: "Carlito", "Calibri", sans-serif;
    background: var(--white);
  }
  .slide-header {
    position: absolute; left: 0; top: 0; width: 1200px; height: 84px;
    background: var(--white);
    border-bottom: 1px solid var(--rule);
  }
  .project-title {
    position: absolute; left: 32px; top: 12px;
    font-family: "Roboto Condensed", "Arial Narrow", sans-serif;
    font-weight: 400; font-size: 52px; line-height: 1;
    color: var(--ink);
  }
  .project-title .accent { color: var(--brand-red); }
  .brand-name {
    position: absolute; right: 14px; top: 14px;
    font-family: "Roboto Condensed", "Arial Narrow", sans-serif;
    font-weight: 700; font-size: 56px; line-height: 1; letter-spacing: 2px;
    color: var(--brand-red);
  }
  .backdrop {
    position: absolute; left: 0; top: 85px; width: 1200px; height: 752px;
    background:
      radial-gradient(ellipse 900px 420px at 1000px 560px, rgba(253,240,241,0.9), rgba(255,255,255,0) 70%),
      linear-gradient(180deg, var(--tint) 0%, #fdf3f4 45%, var(--white) 80%);
  }
  .content-title {
    position: absolute; left: 55px; top: 165px;
    font-family: "Roboto Condensed", "Arial Narrow", sans-serif;
    font-weight: 400; font-size: 42px; line-height: 1;
    color: var(--brand-red);
  }
  .step { position: absolute; left: 60px; width: 1092px; height: 146px; }
  .step-arrow { position: absolute; left: 0; top: 0; width: 147px; height: 146px; }
  .step-label {
    position: absolute; left: 0; top: 58px; width: 147px;
    text-align: center; color: var(--white);
    font-weight: 700; font-size: 25px; line-height: 30px;
  }
  .step-box {
    position: absolute; left: 147px; top: 0; width: 944px; height: 96px;
    background: var(--white);
    border: 1.5px solid var(--brand-red);
    border-radius: 8px;
    padding: 8px 0 0 16px;
    list-style: none;
  }
  .step-box li {
    font-size: 26px; line-height: 39px; color: var(--body-text);
    display: flex; align-items: center;
  }
  .step-box li svg { width: 12px; height: 14px; margin-right: 8px; flex: none; }
  .footer-rule { position: absolute; left: 0; top: 837px; width: 1200px; height: 6px; background: var(--ink); }
  .slide-footer {
    position: absolute; left: 0; top: 845px; width: 1200px; height: 55px;
    background: var(--brand-red); color: var(--white);
    display: flex; justify-content: space-between; align-items: center;
    padding: 0 16px 0 20px; font-size: 20px;
  }
  .page-number { font-weight: 700; }
</style>
</head>
<body>
<div class="slide">
  <div class="backdrop" role="img" aria-label="Soft pink background with a faint fox-shaped wave"></div>

  <header class="slide-header">
    <h1 class="project-title"><span class="accent">Project</span> Title Here</h1>
    <div class="brand-name">DUVNA</div>
  </header>

  <h2 class="content-title">Content Title Here</h2>

  <svg width="0" height="0" style="position:absolute">
    <defs>
      <polygon id="chevron-shape" points="0,0 73.5,40 147,0 147,98 73.5,146 0,98" />
      <polyline id="bullet" points="3,2 9,7 3,12" fill="none" stroke="#333" stroke-width="3" />
    </defs>
  </svg>

  <section class="step" style="top:252px">
    <svg class="step-arrow" viewBox="0 0 147 146"><use href="#chevron-shape" fill="var(--brand-red)"/></svg>
    <div class="step-label">Text Here</div>
    <ul class="step-box">
      <li><svg viewBox="0 0 12 14"><use href="#bullet"/></svg>Lorem ipsum dolor sit ipsum Lorem ipsum dolor sit ipsum Lorem ipsum</li>
      <li><svg viewBox="0 0 12 14"><use href="#bullet"/></svg>Lorem ipsum dolor sit ipsum Lorem ipsum dolor sit ipsum Lorem ipsum</li>
    </ul>
  </section>

  <section class="step" style="top:384px">
    <svg class="step-arrow" viewBox="0 0 147 146"><use href="#chevron-shape" fill="var(--brand-red)"/></svg>
    <div class="step-label">Text Here</div>
    <ul class="step-box">
      <li><svg viewBox="0 0 12 14"><use href="#bullet"/></svg>Lorem ipsum dolor sit ipsum Lorem ipsum dolor sit ipsum Lorem ipsum</li>
      <li><svg viewBox="0 0 12 14"><use href="#bullet"/></svg>Lorem ipsum dolor sit ipsum Lorem ipsum dolor sit ipsum Lorem ipsum</li>
    </ul>
  </section>

  <section class="step" style="top:513px">
    <svg class="step-arrow" viewBox="0 0 147 146"><use href="#chevron-shape" fill="var(--brand-red)"/></svg>
    <div class="step-label">Text Here</div>
    <ul class="step-box">
      <li><svg viewBox="0 0 12 14"><use href="#bullet"/></svg>Lorem ipsum dolor sit ipsum Lorem ipsum dolor sit ipsum Lorem ipsum</li>
      <li><svg viewBox="0 0 12 14"><use href="#bullet"/></svg>Lorem ipsum dolor sit ipsum Lorem ipsum dolor sit ipsum Lorem ipsum</li>
    </ul>
  </section>

  <section class="step" style="top:649px">
    <svg class="step-arrow" viewBox="0 0 147 146"><use href="#chevron-shape" fill="var(--brand-red)"/></svg>
    <div class="step-label">Text Here</div>
    <ul class="step-box">
      <li><svg viewBox="0 0 12 14"><use href="#bullet"/></svg>Lorem ipsum dolor sit ipsum Lorem ipsum dolor sit ipsum Lorem ipsum</li>
      <li><svg viewBox="0 0 12 14"><use href="#bullet"/></svg>Lorem ipsum dolor sit ipsum Lorem ipsum dolor sit ipsum Lorem ipsum</li>
    </ul>
  </section>

  <div class="footer-rule"></div>
  <footer class="slide-footer">
    <span class="copyright">Copyright text here</span>
    <span class="page-number">Page : 01</span>
  </footer>
</div>
</body>
</html>
```